office stationary for pr
pr biz stationery
Creative Brief
Simple
Adaeze Nnorom
14 mabel close eastern lagoonview estate off harmon drive lekki lagos
annorom@pelvora.com
www.pelvora.com
the logo should be used at the back of the business card

```html
<!DOCTYPE html>
<html lang="en">
<head>
<meta charset="utf-8">
<title>pr stationery set</title>
<link rel="stylesheet" href="https://fonts.googleapis.com/css2?family=Lato:wght@300;400&display=swap">
<style>
  :root {
    --backdrop: #e9eaec;
    --paper: #ffffff;
    --paper-edge: #d9dbe0;
    --ink: #5b5f66;
    --ink-soft: #9a9ea6;
    --brand-blue: #3f78b5;
    --brand-light: #a9c4e2;
    --card-tint: #eef2f7;
    --navy: #1f2c49;
    --navy-text: #c7d3e6;
  }
  * { box-sizing: border-box; margin: 0; padding: 0; }
  html, body { width: 1200px; height: 528px; overflow: hidden; }
  body {
    position: relative;
    background: var(--backdrop);
    font-family: "Lato", sans-serif;
    font-weight: 300;
    color: var(--ink);
  }
  address { font-style: normal; }
  .sheet {
    position: absolute;
    background: var(--paper);
    border: 1px solid var(--paper-edge);
  }
  .wordmark {
    font-family: "Lato", sans-serif;
    font-weight: 300;
    color: var(--brand-blue);
    letter-spacing: 0.02em;
    line-height: 1;
  }

  /* Letterhead */
  .letterhead { left: 8px; top: 6px; width: 362px; height: 494px; padding: 28px 28px; font-size: 6.4px; line-height: 1.6; }
  .letterhead .date { margin-bottom: 14px; }
  .letterhead p { margin-bottom: 10px; }
  .letterhead .signoff { margin-top: 16px; }
  .letterhead .footer-mark { position: absolute; left: 28px; bottom: 34px; font-size: 38px; color: var(--brand-light); }
  .letterhead .footer-address { position: absolute; right: 28px; bottom: 36px; text-align: right; font-size: 6.4px; line-height: 1.6; color: var(--brand-blue); }

  /* Business cards */
  .card { top: 28px; width: 128px; height: 62px; padding: 8px 9px; font-size: 5.2px; line-height: 1.5; background: var(--card-tint); }
  .card-front-a { left: 394px; }
  .card-back { left: 536px; background: var(--brand-light); border-color: var(--brand-light); display: flex; align-items: center; justify-content: center; }
  .card-back .wordmark { color: var(--paper); font-size: 18px; }
  .card-front-b { left: 680px; }
  .card .card-name { font-size: 6.4px; color: var(--brand-blue); font-weight: 400; }
  .card .card-role { margin-bottom: 4px; color: var(--ink-soft); }
  .card .card-mark { position: absolute; right: 9px; bottom: 7px; font-size: 10px; }

  /* Envelopes */
  .envelope { left: 392px; width: 424px; height: 190px; padding: 28px 30px; }
  .envelope-top { top: 148px; }
  .envelope-bottom { top: 348px; height: 150px; }
  .envelope .wordmark { font-size: 28px; }
  .envelope .rule { position: absolute; left: 30px; right: 30px; top: 68px; height: 1px; background: var(--brand-light); }
  .envelope-top .return-address { position: absolute; right: 30px; bottom: 22px; text-align: right; font-size: 6.4px; line-height: 1.6; color: var(--brand-blue); }
  .envelope-bottom .return-line { position: absolute; left: 30px; right: 30px; bottom: 16px; font-size: 6px; color: var(--brand-blue); }

  /* Presentation folder */
  .folder { position: absolute; left: 828px; top: 6px; width: 364px; height: 494px; background: var(--navy); }
  .folder .wordmark { position: absolute; left: 150px; top: 208px; font-size: 34px; color: var(--navy-text); }
  .folder .folder-address { position: absolute; left: 196px; top: 258px; font-size: 6.4px; line-height: 1.6; color: var(--navy-text); }
</style>
</head>
<body>

  <article class="sheet letterhead">
    <p class="date">March 12, 2011</p>
    <p>Dear Client,</p>
    <p>Thank you for choosing our studio for your new office stationery. We have prepared a clean and simple set that carries your name with calm confidence across every printed piece.</p>
    <p>Each item uses the same soft blue, light type and generous white space, so letters, cards and envelopes feel like one family on any desk.</p>
    <p>Please review the proofs and share any changes you would like before we send the final files to print.</p>
    <p>The business card carries the mark on its back, while the front keeps your details short and easy to read.</p>
    <p>We look forward to hearing from you soon.</p>
    <p class="signoff">Kind regards,<br>Adaeze Nnorom</p>
    <div class="wordmark footer-mark">pelvora</div>
    <address class="footer-address">27 orchid row<br>willowmere court<br>off castell road<br>brennham<br>www.pelvora.com</address>
  </article>

  <section class="sheet card card-front-a">
    <div class="card-name">Adaeze Nnorom</div>
    <div class="card-role">Creative Director</div>
    <div>annorom@pelvora.com</div>
    <div>www.pelvora.com</div>
    <div class="wordmark card-mark">pelvora</div>
  </section>

  <section class="sheet card card-back">
    <div class="wordmark">pelvora</div>
  </section>

  <section class="sheet card card-front-b">
    <div class="card-name">Adaeze Nnorom</div>
    <div class="card-role">Creative Director</div>
    <div>annorom@pelvora.com</div>
    <div>www.pelvora.com</div>
    <div class="wordmark card-mark">pelvora</div>
  </section>

  <section class="sheet envelope envelope-top">
    <div class="wordmark">pelvora</div>
    <div class="rule"></div>
    <address class="return-address">27 orchid row<br>willowmere court<br>off castell road<br>brennham<br>www.pelvora.com</address>
  </section>

  <section class="sheet envelope envelope-bottom">
    <div class="wordmark">pelvora</div>
    <div class="rule"></div>
    <div class="return-line">27 orchid row, willowmere court, off castell road, brennham &nbsp;·&nbsp; www.pelvora.com</div>
  </section>

  <section class="folder">
    <div class="wordmark">pelvora</div>
    <address class="folder-address">27 orchid row<br>willowmere court<br>off castell road<br>brennham<br>www.pelvora.com</address>
  </section>

</body>
</html>
```